Law Firm Website

We are a small California based law firm specializing in business, corporate and litigation matters. We need to have our website redesigned. We are looking for a new and fresh look for our site, keeping in mind that we are a law firm.
What we don't want:
**the traditional "gavel" and "scales of justice" look
**anything too crazy
What we do want:
**sophisticated yet modern and fresh corporate look and feel
**samples of websites we really like:
http://www.tqmarlow.example
http://www.hembrynoth.example/
we also like:
http://www.fasterlyndqvist.example/
http://www.qp.example/
http://www.ostbury.example/
http://www.pvnd.example
http://www.okrlaw.example/
The content will be whatever is currently on our website (www.marchfieldlawgroup.example). We will be selecting the winner based on originality and keeping the above requirements in mind. Please note that the photos that you use will be the ones that we will be using, so choose wisely because the photos will make a difference.
Target Market(s)
Corporate clients
Industry/Entity Type
Law Firm
Look and feel

```html
<!DOCTYPE html>
<html lang="en">
<head>
<meta charset="utf-8">
<title>Marchfield Law Group, LLP</title>
<link href="https://fonts.googleapis.com/css2?family=Fira+Sans:wght@400;500&family=Oswald:wght@400;500&display=swap" rel="stylesheet">
<style>
:root{
  --bg:#f2f2f2;
  --page:#ffffff;
  --navy:#014a82;
  --tab-1:#7b7b7b;
  --tab-2:#979797;
  --tab-3:#adadad;
  --tab-4:#c6c6c6;
  --teal:#00a9b5;
  --coral:#f26b4f;
  --ink:#2a2a2a;
  --rule:#9a9a9a;
  --footer:#3a3a3a;
  --sky:#8fb6dd;
  --stone:#a89680;
}
*{margin:0;padding:0;box-sizing:border-box}
html,body{width:1200px;height:900px;overflow:hidden;background:var(--bg)}
.page{position:absolute;left:56px;top:128px;width:1090px;height:678px;background:var(--page);box-shadow:0 0 30px rgba(0,0,0,.18)}
.brand{position:absolute;left:66px;top:40px;display:flex;align-items:center;gap:10px}
.brand-mark{width:48px;height:56px;background:var(--navy)}
.brand-name{font-family:"Fira Sans",sans-serif;font-weight:400;font-size:28px;color:var(--ink)}
.nav{position:absolute;right:22px;top:96px;display:flex;gap:2px;list-style:none}
.nav li{width:70px;height:24px;color:#fff;font-family:"Oswald",sans-serif;font-size:13px;text-align:center;line-height:24px;text-transform:uppercase}
.nav .home{background:var(--navy)}
.nav .about{background:var(--tab-1)}
.nav .areas{background:var(--tab-2)}
.nav .links{background:var(--tab-3)}
.nav .contact{background:var(--tab-4)}
.band{position:absolute;left:0;top:120px;width:100%;height:24px;background:var(--navy)}
.hero{position:absolute;left:0;top:144px;width:100%;height:285px;background:linear-gradient(180deg,var(--sky) 0%,#b9cfe6 45%,var(--stone) 46%,#7d7266 100%)}
.hero-caption{position:absolute;left:99px;top:196px;font-family:"Oswald",sans-serif;color:#fff;display:flex;align-items:center;gap:8px;text-transform:uppercase}
.hero-caption .title{font-size:24px;font-weight:500}
.hero-caption .sep{width:2px;height:30px;background:#fff}
.hero-caption .detail{font-size:16px}
.arrow{position:absolute;left:926px;width:29px;height:30px;background:rgba(110,110,110,.75)}
.arrow.next{top:112px}.arrow.prev{top:166px}
.circle{position:absolute;top:486px;width:114px;height:114px;border-radius:50%;color:#fff;font-family:"Oswald",sans-serif;font-size:28px;display:flex;align-items:center;justify-content:center;text-transform:uppercase}
.welcome{left:94px;background:var(--teal)}
.news{left:882px;background:var(--coral)}
.divider{position:absolute;left:231px;top:472px;width:2px;height:144px;background:var(--rule)}
.intro{position:absolute;left:256px;top:461px;width:530px;font-family:"Fira Sans",sans-serif;font-size:10px;line-height:13.7px;color:var(--ink)}
.intro p+p{margin-top:13.7px}
.footer{position:absolute;left:0;bottom:0;width:100%;height:10px;background:var(--footer)}
</style>
</head>
<body>
<div class="page">
  <header>
    <div class="brand"><span class="brand-mark"></span><span class="brand-name">Marchfield Law Group, LLP</span></div>
    <ul class="nav">
      <li class="home">Home</li><li class="about">About Us</li><li class="areas">Areas</li><li class="links">Links</li><li class="contact">Contact</li>
    </ul>
  </header>
  <div class="band"></div>
  <section class="hero" role="img" aria-label="Photo of a modern civic building with a clock tower and a hanging flag under a blue sky">
    <div class="hero-caption"><span class="title">Headline</span><span class="sep"></span><span class="detail">Details of the headline</span></div>
    <svg class="arrow next" viewBox="0 0 29 30"><polyline points="10,8 19,15 10,22" fill="none" stroke="#fff" stroke-width="2.5"/></svg>
    <svg class="arrow prev" viewBox="0 0 29 30"><polyline points="19,8 10,15 19,22" fill="none" stroke="#fff" stroke-width="2.5"/></svg>
  </section>
  <div class="circle welcome">Welcome</div>
  <div class="divider"></div>
  <div class="intro">
    <p>Marchfield Law Group, LLP provides quality legal representation to corporate as well as individual clients in the areas of business, corporate, securities, products liability, civil litigation (in State and Federal Courts), Alternative Dispute Resolution (arbitration and mediation), as well as a host of transactional matters.</p>
    <p>Our attorneys are committed to providing zealous advocacy in litigation, as well as creative approaches to difficult challenges that face our business clients. Our goal is to provide the highest level of representation and personal service to each and every client, and to meet and exceed each client's expectations. We take the time to explore and explain all viable options and keep our clients informed at every step of their legal matter.</p>
    <p>We encourage you to contact us to discuss the development of a professional relationship. If you seek a firm that is experienced and committed to representing your best interests, then look no further.</p>
  </div>
  <div class="circle news">News</div>
  <div class="footer"></div>
</div>
</body>
</html>
```